Tend Your Harvest - Keep your Bloom - The freedom to choose and participate in your own path to hea

I have a logo that needs to be turned into a large banner for my website. I want to keep the same font in the uploaded logo image. Now this image could stay at the top of the header kind of where it is now on the web site, It doesn't have to be the main thing on the page. I want this header to be artistic - alive, healthy, joyous - colorful banner that shows wellness, healing, vitality and hope.
If you had a chronic illness and came to my site what would you want to see? You'd want to feel empowered, enlightened, engaged, hopeful and feel the love, right?.
I look forward to getting your creative ideas and designs.

Target Market(s)

People struggling with illness who are looking for a better quality of life. We provide training and education on how to do that. Hope, happiness - healing - Vitality - whole natural foods - mediation - visualization - whole health.

Industry/Entity Type

Health And Wellness

Logo Text

Tend Your Harvest with the koru and with Marigold Thwaite (use the font on the uploaded file)

Requirements
Must have
• I've changed the photos in this order. You can pick up options here:
• https://www.filebarrow.example/s/x7pleqnrtwz2kdm/IMG_4402%20%20high%20resolution.jpg?dl=0
• https://www.filebarrow.example/s/m3bvohqyeuc8zta/IMG_4587%20high%20resolution.jpg?dl=0
• My original logo - Tend Your Harvest - Marigold Thwaite
• "Together we make tragic moments magic moments" Join us (sign up type button)
Nice to have
• Something stunningly simple, classy, inviting, where my message gets across.
• Here's a similar website to mine: http://dalvenhope.example
• I need a link to join up somewhere - with my quote.
• "My tragic moments have become magic moments" Join us (sign up type button)
Should not have
• I do not want other people in the header.
• No crunchy granola feel!
• This is gone mainstream now.

```html
<!DOCTYPE html>
<html lang="en">
<head>
<meta charset="utf-8">
<title>Tend Your Harvest with Marigold Thwaite</title>
<link rel="stylesheet" href="https://fonts.googleapis.com/css2?family=Raleway:wght@400;700&family=Noto+Serif:ital,wght@1,700&family=Open+Sans:wght@700&display=swap">
<style>
  :root {
    --forest-light: #c9d86a;
    --forest-mid: #7d9a3a;
    --forest-deep: #3f5a22;
    --slate-dark: #2b3845;
    --slate-mid: #56626e;
    --slate-light: #b7bdc5;
    --teal-pale: #8dd2d2;
    --teal: #5db7ba;
    --teal-deep: #2c8790;
    --title-teal: #6cc1c5;
    --name-blue: #3f7fd0;
    --ring-dark: #2f3416;
    --gold: #cdb85c;
    --button-green: #5fae3a;
    --button-green-dark: #3f8a22;
    --white: #ffffff;
  }
  html, body {
    margin: 0;
    padding: 0;
    overflow: hidden;
    background: #ffffff;
  }
  .banner {
    position: relative;
    width: 1200px;
    height: 440px;
    overflow: hidden;
    font-family: "Raleway", Arial, sans-serif;
  }
  .forest-backdrop {
    position: absolute;
    inset: 0;
    background:
      radial-gradient(ellipse 260px 180px at 120px 60px, #e9ef9a 0%, transparent 70%),
      radial-gradient(ellipse 300px 200px at 1080px 250px, #d4e06a 0%, transparent 70%),
      radial-gradient(ellipse 400px 220px at 650px 120px, var(--forest-deep) 0%, transparent 75%),
      linear-gradient(120deg, var(--forest-light) 0%, var(--forest-mid) 35%, var(--forest-deep) 60%, var(--forest-mid) 100%);
  }
  .shapes {
    position: absolute;
    inset: 0;
  }
  .title {
    position: absolute;
    left: 512px;
    top: 22px;
    margin: 0;
    font-weight: 400;
    font-size: 47px;
    letter-spacing: 0.5px;
    color: var(--title-teal);
    white-space: nowrap;
  }
  .title sup {
    font-size: 12px;
    vertical-align: 30px;
  }
  .with-line {
    position: absolute;
    left: 514px;
    top: 86px;
    display: flex;
    align-items: baseline;
    gap: 12px;
    white-space: nowrap;
  }
  .with-line .with {
    font-weight: 700;
    font-size: 25px;
    color: var(--title-teal);
  }
  .with-line .name {
    font-weight: 400;
    font-size: 40px;
    color: var(--name-blue);
  }
  .tagline {
    position: absolute;
    left: 592px;
    width: 400px;
    top: 229px;
    margin: 0;
    text-align: center;
    font-family: "Noto Serif", Georgia, serif;
    font-style: italic;
    font-weight: 700;
    font-size: 24px;
    line-height: 32px;
    letter-spacing: 1px;
    color: var(--white);
  }
  .site-url {
    position: absolute;
    left: 540px;
    top: 380px;
    font-family: "Open Sans", Arial, sans-serif;
    font-weight: 700;
    font-size: 16px;
    letter-spacing: 0.5px;
    color: var(--white);
    text-decoration: none;
  }
  .join-button {
    position: absolute;
    left: 918px;
    top: 344px;
    width: 188px;
    height: 40px;
    box-sizing: border-box;
    border-radius: 20px;
    border: 2px solid #e6f0d8;
    background: linear-gradient(180deg, #7cc457 0%, var(--button-green) 50%, var(--button-green-dark) 100%);
    box-shadow: 0 3px 6px rgba(0,0,0,0.35);
    display: flex;
    align-items: center;
    padding-left: 8px;
    gap: 20px;
    font-family: "Open Sans", Arial, sans-serif;
    font-weight: 700;
    font-size: 18px;
    letter-spacing: 1px;
    color: var(--white);
    text-decoration: none;
  }
  .join-button svg { flex: none; }
</style>
</head>
<body>
<div class="banner">
  <div class="forest-backdrop" role="img" aria-label="Softly blurred sunlit green forest background"></div>

  <svg class="shapes" width="1200" height="440" viewBox="0 0 1200 440" aria-hidden="true">
    <defs>
      <linearGradient id="slateFill" x1="0" y1="0" x2="1" y2="0">
        <stop offset="0" stop-color="var(--slate-dark)"/>
        <stop offset="0.45" stop-color="var(--slate-mid)"/>
        <stop offset="1" stop-color="var(--slate-light)"/>
      </linearGradient>
      <linearGradient id="tealBand" x1="0" y1="0" x2="1" y2="0">
        <stop offset="0" stop-color="var(--teal)"/>
        <stop offset="1" stop-color="var(--teal-deep)"/>
      </linearGradient>
      <linearGradient id="ringFill" x1="0" y1="0" x2="1" y2="1">
        <stop offset="0" stop-color="#4b5220"/>
        <stop offset="1" stop-color="var(--ring-dark)"/>
      </linearGradient>
    </defs>

    <!-- lower slate field -->
    <path d="M0,100 C150,160 300,250 560,300 C820,345 1040,240 1200,168 L1200,440 L0,440 Z" fill="url(#slateFill)"/>
    <path d="M0,300 L360,440 L0,440 Z" fill="#26313c" opacity="0.5"/>

    <!-- left pale teal ribbon -->
    <path d="M0,70 C80,92 150,122 230,160 L230,190 C150,152 80,124 0,102 Z" fill="var(--teal-pale)"/>
    <path d="M0,102 C80,124 150,152 230,190" fill="none" stroke="var(--gold)" stroke-width="2"/>

    <!-- main teal ribbon -->
    <path d="M360,196 C620,262 960,232 1200,146 L1200,194 C960,292 640,334 360,304 Z" fill="url(#tealBand)"/>
    <path d="M360,304 C640,334 960,292 1200,194" fill="none" stroke="var(--gold)" stroke-width="3"/>

    <!-- portrait ring -->
    <circle cx="302" cy="207" r="170" fill="url(#ringFill)"/>
    <circle cx="302" cy="207" r="170" fill="none" stroke="var(--gold)" stroke-width="2" opacity="0.7"/>
    <circle cx="302" cy="207" r="159" fill="var(--teal-pale)"/>
    <circle cx="302" cy="207" r="155" fill="#b79a7e" role="img" aria-label="Portrait photo of Marigold Thwaite"/>

    <!-- plain mark beside the title -->
    <circle cx="1076" cy="80" r="24" fill="none" stroke="#2aa8d8" stroke-width="6"/>
  </svg>

  <h1 class="title">Tend Your Harvest<sup>™</sup></h1>
  <div class="with-line">
    <span class="with">With</span>
    <span class="name">Marigold Thwaite</span>
  </div>

  <p class="tagline">wellness, healing, vitality and hope.</p>

  <a class="site-url" href="#">www.Yoururl.com</a>

  <a class="join-button" href="#">
    <svg width="26" height="26" viewBox="0 0 26 26" aria-hidden="true">
      <circle cx="13" cy="13" r="13" fill="#1f2a18"/>
      <path d="M10,7 L16,13 L10,19" fill="none" stroke="#ffffff" stroke-width="3" stroke-linecap="round" stroke-linejoin="round"/>
    </svg>
    JOIN NOW
  </a>
</div>
</body>
</html>
```